arts & crafts

I collect old plates & make them into serving plates for cakes, afternoon teas, special occasions, weddings, parties, bridal showers. cake competitions, displays in bakeries.

Contact Information for Business Card

Tulips Turn Gold
Bringing the old back to new
Ph 0417283956
info@ tulipsturngold.com.au
www.tulipsturngold.com.au
pagebook
Craftlo

```html
<!DOCTYPE html>
<html lang="en">
<head>
<meta charset="utf-8">
<title>Tulips Turn Gold – Business Cards</title>
<link rel="stylesheet" href="https://fonts.googleapis.com/css2?family=Marcellus&display=swap">
<style>
  :root {
    --page: #ffffff;
    --card-blue: #4f80c0;
    --card-periwinkle: #6a80bf;
    --band-blue: #7fa2d6;
    --band-periwinkle: #8ea0d4;
    --plate: #e9eef9;
    --plate-ring: #b9c8e8;
    --ink-blue: #3d5aa8;
    --white: #ffffff;
  }
  html, body {
    margin: 0;
    padding: 0;
    width: 972px;
    height: 1200px;
    overflow: hidden;
    background: var(--page);
  }
  .sheet { display: block; width: 972px; height: 1200px; }
  .brand-text, .tagline, .contact-text, .social-name {
    font-family: "Marcellus", Georgia, serif;
  }
  .brand-text { fill: var(--ink-blue); font-size: 34px; }
  .tagline { fill: var(--ink-blue); font-size: 19px; }
  .contact-text { fill: var(--white); font-size: 20px; }
  .social-name { fill: var(--white); font-size: 18px; }
  .icon { fill: none; stroke: var(--white); stroke-width: 1.6; }
  .social-dot { fill: var(--white); }
  .plate { fill: var(--plate); stroke: var(--plate-ring); stroke-width: 3; }
</style>
</head>
<body>
<svg class="sheet" viewBox="0 0 1002 1237" xmlns="http://www.w3.org/2000/svg">
  <defs>
    <filter id="card-shadow" x="-10%" y="-10%" width="120%" height="130%">
      <feDropShadow dx="0" dy="8" stdDeviation="9" flood-color="#000" flood-opacity="0.28"/>
    </filter>
    <clipPath id="clip-front"><rect x="128" y="95" width="740" height="455" rx="32"/></clipPath>
    <clipPath id="clip-back"><rect x="126" y="658" width="740" height="455" rx="32"/></clipPath>
    <path id="tagline-arc" d="M 161.5 880 A 160 160 0 0 0 468.5 880"/>
  </defs>

  <!-- Card one -->
  <g class="card card-front">
    <rect x="128" y="95" width="740" height="455" rx="32" fill="var(--card-blue)" filter="url(#card-shadow)"/>
    <g clip-path="url(#clip-front)">
      <circle cx="231" cy="322" r="272" fill="var(--band-blue)" role="img" aria-label="Scalloped ornamental porcelain-style border band"/>
      <circle cx="231" cy="322" r="240" fill="var(--white)"/>
    </g>
    <g class="logo">
      <circle class="plate" cx="305" cy="290" r="115"/>
      <text class="brand-text" x="305" y="282" text-anchor="middle">Tulips</text>
      <text class="brand-text" x="305" y="322" text-anchor="middle">Turn Gold</text>
    </g>
    <text class="tagline" x="308" y="446" text-anchor="middle">BRINGING THE OLD BACK TO NEW</text>

    <g class="socials">
      <circle class="social-dot" cx="630" cy="274" r="6"/>
      <text class="social-name" x="642" y="280">Craftlo</text>
      <circle class="social-dot" cx="718" cy="274" r="6"/>
      <text class="social-name" x="730" y="280">pagebook</text>
    </g>

    <g class="contacts">
      <rect class="icon" x="542" y="404" width="11" height="18" rx="2"/>
      <line class="icon" x1="546" y1="418" x2="549" y2="418"/>
      <text class="contact-text" x="574" y="422">0417283956</text>

      <rect class="icon" x="538" y="440" width="20" height="13" rx="1"/>
      <polyline class="icon" points="538,440 548,448 558,440"/>
      <text class="contact-text" x="574" y="454">info@ tulipsturngold.com.au</text>

      <circle class="icon" cx="548" cy="478" r="10"/>
      <ellipse class="icon" cx="548" cy="478" rx="4.5" ry="10"/>
      <line class="icon" x1="538" y1="478" x2="558" y2="478"/>
      <text class="contact-text" x="574" y="485">www.tulipsturngold.com.au</text>
    </g>
  </g>

  <!-- Card two -->
  <g class="card card-back">
    <rect x="126" y="658" width="740" height="455" rx="32" fill="var(--card-periwinkle)" filter="url(#card-shadow)"/>
    <g clip-path="url(#clip-back)">
      <circle cx="305" cy="780" r="267" fill="var(--band-periwinkle)" role="img" aria-label="Scalloped ornamental porcelain-style border band"/>
      <circle cx="305" cy="780" r="235" fill="var(--white)"/>
    </g>
    <g class="logo">
      <circle class="plate" cx="305" cy="815" r="115"/>
      <text class="brand-text" x="305" y="807" text-anchor="middle">Tulips</text>
      <text class="brand-text" x="305" y="847" text-anchor="middle">Turn Gold</text>
    </g>
    <text class="tagline"><textPath href="#tagline-arc" startOffset="50%" text-anchor="middle">BRINGING THE OLD BACK TO NEW</textPath></text>

    <g class="socials">
      <circle class="social-dot" cx="630" cy="910" r="6"/>
      <text class="social-name" x="642" y="916">Craftlo</text>
      <circle class="social-dot" cx="718" cy="910" r="6"/>
      <text class="social-name" x="730" y="916">pagebook</text>
    </g>

    <g class="contacts">
      <rect class="icon" x="542" y="989" width="11" height="18" rx="2"/>
      <line class="icon" x1="546" y1="1003" x2="549" y2="1003"/>
      <text class="contact-text" x="574" y="1007">0417283956</text>

      <rect class="icon" x="538" y="1025" width="20" height="13" rx="1"/>
      <polyline class="icon" points="538,1025 548,1033 558,1025"/>
      <text class="contact-text" x="574" y="1039">info@ tulipsturngold.com.au</text>

      <circle class="icon" cx="548" cy="1063" r="10"/>
      <ellipse class="icon" cx="548" cy="1063" rx="4.5" ry="10"/>
      <line class="icon" x1="538" y1="1063" x2="558" y2="1063"/>
      <text class="contact-text" x="574" y="1070">www.tulipsturngold.com.au</text>
    </g>
  </g>
</svg>
</body>
</html>
```